Bluetooth Earphone Packaging Design

We want to use the packaging for 4-5 of our Bluetooth Earphone series (Picture enclosed) and hence we would not like to put any product pictures on the packaging.

Material: E-Flute Paper box
Type: Window Box style
Design features we prefer: Colorful, creative, trendy, High tech.
Requirement: AI file is preferred
Size of Packaging: (L) 95 x (W) 40 x (H) 120 mm

Enclosed are a detailed description along with competitor designs for your reference.

Any further questions, please feel free to ask

```html
<!DOCTYPE html>
<html lang="en">
<head>
<meta charset="utf-8">
<title>Bluetooth Earphone 5.0 — Packaging Dieline Faces</title>
<link rel="stylesheet" href="https://fonts.googleapis.com/css2?family=Poppins:wght@700&family=Questrial&family=Raleway:wght@200&display=swap">
<style>
  :root {
    --stage: #e4e5e7;
    --paper: #f6f7f5;
    --fold: #dcdedc;
    --title-blue: #1f5f93;
    --band-deep: #1d3f7a;
    --band-mid: #1f5e9a;
    --band-light: #2a7bb4;
    --ink: #1c1c1c;
    --spec-grey: #8d8f91;
    --version-grey: #8a8a8a;
    --window-line: #c9cbcd;
    --trace: #e8eaea;
  }
  * { margin: 0; padding: 0; box-sizing: border-box; }
  html, body {
    width: 1200px; height: 1148px; overflow: hidden;
    background: var(--stage);
  }
  .canvas { position: relative; width: 1200px; height: 1148px; }

  .box-net {
    position: absolute; left: 94px; top: 124px;
    width: 1012px; height: 900px;
    display: flex;
    box-shadow: 0 10px 30px rgba(0,0,0,.12);
  }

  /* ---------- side face ---------- */
  .side-face {
    position: relative; width: 300px; height: 900px;
    background: var(--paper);
    border-right: 1px solid var(--fold);
    overflow: hidden;
  }
  .side-face .trace-area {
    position: absolute; right: 0; top: 0; width: 110px; height: 420px;
    background: linear-gradient(180deg, var(--trace), rgba(246,247,245,0));
  }
  .product-title {
    position: absolute; left: 65px; top: 148px;
    writing-mode: vertical-rl;
    font-family: "Poppins", sans-serif; font-weight: 700;
    font-size: 62px; line-height: 78px;
    color: var(--title-blue); letter-spacing: 0.5px;
  }
  .version-mark {
    position: absolute; left: 82px; top: 556px;
    writing-mode: vertical-rl;
    font-family: "Raleway", sans-serif; font-weight: 200;
    font-size: 190px; line-height: 150px;
    color: var(--version-grey);
  }

  /* ---------- back face ---------- */
  .back-face {
    position: relative; width: 712px; height: 900px;
    background: var(--paper); overflow: hidden;
  }
  .back-face .trace-area {
    position: absolute; left: 0; top: 0; width: 560px; height: 560px;
    background: radial-gradient(ellipse at 50% 0%, var(--trace), rgba(246,247,245,0) 70%);
  }
  .accent-band { position: absolute; right: 0; top: 0; width: 150px; height: 900px; }

  .spec-list {
    position: absolute; left: 32px; top: 128px;
    font-family: "Questrial", sans-serif; font-size: 17px; line-height: 22px;
    color: var(--spec-grey); list-style: none;
  }
  .spec-list .spec-heading {
    font-family: "Poppins", sans-serif; font-weight: 700;
    color: var(--ink); font-size: 16px;
  }

  .display-window {
    position: absolute; left: 40px; top: 430px; width: 340px; height: 170px;
    border: 1.5px solid var(--window-line);
  }

  .product-notes { position: absolute; left: 32px; top: 648px; width: 560px; }
  .product-notes h2 {
    font-family: "Poppins", sans-serif; font-weight: 700;
    font-size: 13px; color: var(--ink); margin-bottom: 6px;
  }
  .product-notes p {
    font-family: "Questrial", sans-serif; font-size: 10.5px; line-height: 15px;
    color: #6f7173;
  }

  .compliance-marks {
    position: absolute; left: 34px; top: 780px;
    display: flex; gap: 22px; align-items: center;
  }
</style>
</head>
<body>
<div class="canvas">
  <div class="box-net">

    <section class="side-face">
      <div class="trace-area" role="img" aria-label="Faint grey circuit-board trace pattern"></div>
      <h1 class="product-title">Bluetooth<br>Earphone</h1>
      <div class="version-mark">5.0</div>
    </section>

    <section class="back-face">
      <div class="trace-area" role="img" aria-label="Faint grey circuit-board trace pattern"></div>

      <svg class="accent-band" viewBox="0 0 150 900" role="img" aria-label="Blue accent band with circuit-board pattern">
        <defs>
          <linearGradient id="band-fill" x1="0" y1="0" x2="0" y2="1">
            <stop offset="0" stop-color="var(--band-light)"/>
            <stop offset="0.5" stop-color="var(--band-mid)"/>
            <stop offset="1" stop-color="var(--band-deep)"/>
          </linearGradient>
        </defs>
        <polygon points="0,0 150,0 150,900 120,900" fill="url(#band-fill)"/>
      </svg>

      <ul class="spec-list">
        <li class="spec-heading">Specification:</li>
        <li>Bluetooth Version: 5.0</li>
        <li>Wireless Playback Duration: 3-4 h</li>
        <li>Standby Time: 80 h</li>
        <li>Wireless Range: 10 m</li>
        <li>Impedance: 32 Ω</li>
        <li>Sound Pressure Level: 100dB ± 3dB</li>
        <li>Frequency Response: 20-20kHz</li>
        <li>Driver Unit: 10mm</li>
      </ul>

      <div class="display-window"></div>

      <div class="product-notes">
        <h2>Bluetooth Earphone 5.0</h2>
        <p>These wireless earphones pair quickly with phones, tablets and laptops, giving clear stereo sound, deep bass and steady calls. The light shell sits securely in the ear for sport, travel and daily use. Charge fully before first use, keep away from water and heat, and store in the case when not in use to protect the battery and extend its service life.</p>
      </div>

      <svg class="compliance-marks" width="260" height="50" viewBox="0 0 260 50" aria-label="Compliance marks">
        <circle cx="22" cy="25" r="19" fill="none" stroke="var(--ink)" stroke-width="4"/>
        <rect x="70" y="6" width="38" height="38" fill="none" stroke="var(--ink)" stroke-width="4"/>
        <circle cx="150" cy="25" r="19" fill="var(--ink)"/>
        <rect x="193" y="6" width="38" height="38" rx="6" fill="none" stroke="var(--ink)" stroke-width="4"/>
      </svg>
    </section>

  </div>
</div>
</body>
</html>
```